Natural Skin Care e commerce website

we are the distributor for natural skincare product , we would like to develop a e commerce website which encompass the ability to divide the product into face, body , baby , and base on ingredient , best seller, we are Verdal certified product the key point to focus is natural organic , no nasties, vegan , unpolluted , full of natural ingredient. manuka, olive nordic style temporary style website is preferred. the website name is Qelvora store.co , the web must have ability to take the order and let the brand upload their products

```html
<!DOCTYPE html>
<html lang="en">
<head>
<meta charset="utf-8">
<title>Qelvora Store – Natural Skin Care</title>
<link rel="stylesheet" href="https://fonts.googleapis.com/css2?family=Montserrat:wght@400;600;700;800&family=Open+Sans:wght@400;600;700&display=swap">
<style>
:root{
  --green:#4f8f1c;
  --green-dark:#3d7512;
  --green-nav:#5c9c22;
  --yellow:#f2b705;
  --ink:#222;
  --muted:#777;
  --line:#e3e3e3;
  --soft:#f4f4f4;
  --white:#fff;
}
*{margin:0;padding:0;box-sizing:border-box}
html,body{width:1200px;height:2952px;overflow:hidden;background:var(--white)}
body{font-family:"Open Sans",Arial,sans-serif;color:var(--ink);position:relative}
.abs{position:absolute}

/* top bar */
.topbar{left:0;top:0;width:1200px;height:48px;background:var(--soft);border-bottom:1px solid var(--line);display:flex;justify-content:center;gap:90px;align-items:center;font-size:12px;font-weight:600;color:#555;letter-spacing:.3px}
.topbar span{display:flex;align-items:center;gap:8px}
.topbar svg{width:14px;height:14px}

/* wordmark: plain text, one colour, one weight, with one plain square */
.wordmark{display:flex;align-items:center;gap:10px;font-family:"Open Sans",Arial,sans-serif;font-weight:700;font-size:28px;color:var(--ink);line-height:1;white-space:nowrap}
.wordmark i{display:block;width:18px;height:18px;background:var(--green)}
.logo{left:148px;top:72px}

.search{left:400px;top:64px;width:462px;height:44px;border:1px solid #ccc;display:flex}
.search .field{flex:1;font-size:13px;color:#999;padding:12px 14px}
.search .cat{width:130px;border-left:1px solid #ccc;font-size:12px;color:#666;padding:13px 12px;display:flex;justify-content:space-between}
.search .go{width:50px;background:var(--yellow);display:flex;align-items:center;justify-content:center}
.social{left:938px;top:66px;display:flex;gap:12px}
.social i{width:38px;height:38px;border-radius:50%;background:#3a3a3a;display:block}

/* nav */
.nav{left:0;top:132px;width:1200px;height:50px;background:var(--green-nav)}
.nav ul{list-style:none;display:flex;position:absolute;left:136px;top:0;height:50px}
.nav li{color:#fff;font-family:"Montserrat",sans-serif;font-weight:600;font-size:13px;padding:0 24px;line-height:50px}
.nav li.active{background:var(--green-dark)}
.cart{right:128px;top:0;height:50px;width:150px;background:var(--yellow);color:#fff;font-family:"Montserrat",sans-serif;font-weight:700;font-size:13px;display:flex;align-items:center;justify-content:center;gap:8px}

/* hero */
.hero{left:0;top:182px;width:1200px;height:460px;background:linear-gradient(90deg,#dfe5d4 0%,#eef0ec 25%,#f1f0ee 55%,#ead8cc 80%,#dcc2b2 100%)}
.hero-olive{left:0;top:182px;width:420px;height:380px;background:radial-gradient(ellipse at 40% 45%,#a9b969 0%,#c9d2a4 45%,rgba(223,229,212,0) 75%)}
.hero-model{left:760px;top:182px;width:440px;height:460px;background:radial-gradient(ellipse at 50% 55%,#e9c1a6 0%,#dfb7a0 40%,rgba(220,194,178,0) 75%)}
.hero-copy{left:444px;top:290px}
.hero-kicker{font-family:"Montserrat",sans-serif;font-weight:700;color:var(--green);font-size:18px}
.hero-title{font-family:"Montserrat",sans-serif;font-weight:700;font-size:54px;line-height:1.1;color:#222;margin-top:6px}
.hero-sub{font-family:"Montserrat",sans-serif;font-weight:400;font-size:42px;color:#333;line-height:1.2}
.hero-cta{font-family:"Montserrat",sans-serif;font-weight:800;font-size:30px;color:var(--yellow);margin-top:18px}
.hero-arrow{top:374px;width:46px;height:46px;border-radius:50%;background:rgba(120,120,120,.55);display:flex;align-items:center;justify-content:center}

/* category tiles */
.tile{top:696px;width:286px;height:216px;overflow:hidden;border:1px solid var(--line)}
.tile .photo{position:absolute;right:0;top:0;width:150px;height:216px}
.tile .txt{position:absolute;left:14px;top:62px;font-family:"Montserrat",sans-serif}
.tile .small{font-size:18px;font-weight:400;color:#333}
.tile .big{font-size:20px;font-weight:800;color:#222}
.btn{display:inline-block;background:var(--green);color:#fff;font-size:11px;font-weight:700;padding:7px 14px;border-radius:2px}
.tile .btn{margin-top:10px}

.rule{left:148px;width:904px;height:1px;background:var(--line)}
.section-title{left:152px;font-family:"Montserrat",sans-serif;font-weight:800;font-size:28px;color:#222;letter-spacing:.5px}
.section-title::after{content:"";display:block;width:90px;height:3px;background:var(--green);margin-top:8px}
.pager{display:flex;gap:8px}
.pager i{width:28px;height:28px;border-radius:50%;background:#e6e6e6;display:flex;align-items:center;justify-content:center}

/* product cards */
.product{width:204px}
.product .img{height:236px;background:var(--soft)}
.product .name{font-family:"Montserrat",sans-serif;font-weight:600;font-size:14px;margin-top:20px}
.product .price{font-family:"Montserrat",sans-serif;font-size:20px;color:#333;margin-top:10px}
.product .stars{color:var(--yellow);font-size:14px;letter-spacing:2px;margin-top:2px}
.product .stars b{color:#ccc;font-weight:400}
.product .btn{margin-top:12px}

.babies{left:608px;top:1080px;width:432px;height:384px;background:linear-gradient(135deg,#e8ddd3 0%,#f3ece6 45%,#d8c7b8 100%)}
.babies-copy{left:708px;top:1196px;width:232px;text-align:center}
.babies-copy h3{font-family:"Montserrat",sans-serif;font-weight:700;font-size:30px;color:#fff;letter-spacing:1px}
.babies-copy .btn{margin-top:14px;font-size:13px;padding:10px 22px}

/* blog */
.blog-band{left:0;top:2120px;width:1200px;height:420px;background:#fafafa}
.post{width:282px}
.post .img{height:164px;position:relative}
.post .date{position:absolute;left:0;bottom:0;width:52px;height:56px;background:var(--green);color:#fff;text-align:center;font-family:"Montserrat",sans-serif;font-weight:700;font-size:22px;line-height:1;padding-top:8px}
.post .date small{display:block;font-size:11px;margin-top:3px}
.post h4{font-family:"Montserrat",sans-serif;font-weight:700;font-size:13px;margin-top:22px}
.post p{font-size:12px;line-height:1.6;color:var(--muted);margin-top:10px}

/* footer */
.footer{left:0;top:2556px;width:1200px;height:356px;background:var(--soft);border-top:1px solid var(--line)}
.f-logo{left:152px;top:2608px}
.f-logo.wordmark{font-size:24px}
.f-logo.wordmark i{width:16px;height:16px}
.newsletter{left:406px;top:2612px;font-family:"Montserrat",sans-serif;font-weight:700;font-size:17px}
.email{left:720px;top:2598px;width:248px;height:46px;background:#fff;border:1px solid #ddd;font-size:13px;color:#999;padding:13px 14px}
.submit{left:968px;top:2598px;width:84px;height:46px;background:var(--green);color:#fff;font-family:"Montserrat",sans-serif;font-weight:700;font-size:13px;display:flex;align-items:center;justify-content:center}
.f-about{left:152px;top:2668px;width:200px;font-size:12px;line-height:1.7;color:var(--muted)}
.f-col h5{font-family:"Montserrat",sans-serif;font-weight:700;font-size:12px;margin-bottom:16px}
.f-col li{list-style:none;font-size:12px;color:#666;margin-bottom:9px;display:flex;align-items:center;gap:8px}
.f-col li::before{content:"";width:4px;height:4px;background:#999;border-radius:50%}
.f-col.info li::before{display:none}
.f-col.info li{align-items:flex-start}
.f-col.info svg{flex:none;margin-top:2px}
.copyright{left:0;top:2912px;width:1200px;height:40px;text-align:center;font-size:12px;color:#777;line-height:40px;border-top:1px solid var(--line)}
</style>
</head>
<body>

<div class="abs topbar">
  <span><svg viewBox="0 0 16 16"><path d="M1 4h9v7H1zM10 7h3l2 2v2h-5z" fill="#5c9c22"/></svg>FREE SHIPPING ON ALL ORDER</span>
  <span><svg viewBox="0 0 16 16"><path d="M3 8l3 3 7-7" stroke="#5c9c22" stroke-width="2" fill="none"/></svg>100% MONEY BACK GUARANTEE</span>
  <span><svg viewBox="0 0 16 16"><circle cx="8" cy="8" r="6" stroke="#5c9c22" stroke-width="2" fill="none"/><path d="M8 5v3l2 2" stroke="#5c9c22" stroke-width="1.5" fill="none"/></svg>ONLINE SUPPORT 24/7</span>
</div>

<header>
  <div class="abs logo wordmark"><i></i>Qelvora Store</div>
  <div class="abs search">
    <div class="field">Search</div>
    <div class="cat">All Categories <span>▾</span></div>
    <div class="go"><svg width="18" height="18" viewBox="0 0 18 18"><circle cx="7.5" cy="7.5" r="5.5" stroke="#fff" stroke-width="2" fill="none"/><path d="M12 12l5 5" stroke="#fff" stroke-width="2"/></svg></div>
  </div>
  <div class="abs social"><i></i><i></i><i></i><i></i></div>
</header>

<nav class="abs nav">
  <ul>
    <li class="active">FOR FACE</li><li>FOR BODY</li><li>FOR SKIN</li><li>FOR BABY</li><li>NEW DEALS</li>
  </ul>
  <div class="abs cart"><svg width="16" height="16" viewBox="0 0 16 16"><path d="M1 2h3l2 8h8l1-6H5" stroke="#fff" stroke-width="1.6" fill="none"/><circle cx="7" cy="13.5" r="1.3" fill="#fff"/><circle cx="13" cy="13.5" r="1.3" fill="#fff"/></svg>CART (0)</div>
</nav>

<section>
  <div class="abs hero"></div>
  <div class="abs hero-olive" role="img" aria-label="Olive branch with green olives and a drop of oil"></div>
  <div class="abs hero-model" role="img" aria-label="Woman with glowing clear skin smiling"></div>
  <div class="abs hero-copy">
    <div class="hero-kicker">NEW OFFERS !</div>
    <div class="hero-title">We Care for</div>
    <div class="hero-sub">your Skin Naturally</div>
    <div class="hero-cta">SHOP NOW</div>
  </div>
  <div class="abs hero-arrow" style="left:14px"><svg width="14" height="14" viewBox="0 0 14 14"><path d="M9 2L4 7l5 5" stroke="#fff" stroke-width="2" fill="none"/></svg></div>
  <div class="abs hero-arrow" style="left:1140px"><svg width="14" height="14" viewBox="0 0 14 14"><path d="M5 2l5 5-5 5" stroke="#fff" stroke-width="2" fill="none"/></svg></div>
</section>

<section>
  <div class="abs tile" style="left:148px;background:#f3e5dc">
    <div class="photo" role="img" aria-label="Woman applying skin care cream" style="background:linear-gradient(180deg,#e8cbb8,#d9ad95)"></div>
    <div class="txt"><div class="small">SKIN CARE</div><div class="big">PRODUCTS</div><span class="btn">Click Here</span></div>
  </div>
  <div class="abs tile" style="left:456px;background:#eef0f2">
    <div class="photo" role="img" aria-label="Woman holding body lotion bottle" style="background:linear-gradient(180deg,#dfe3e8,#cdb8ab)"></div>
    <div class="txt"><div class="small">BODY</div><div class="big">LOTIONS</div><span class="btn">Click Here</span></div>
  </div>
  <div class="abs tile" style="left:762px;background:#f6ece4">
    <div class="photo" role="img" aria-label="Face care tubes and bottles" style="background:linear-gradient(180deg,#f2d9c4,#f0b78a)"></div>
    <div class="txt"><div class="small">FACE</div><div class="big">PRODUCTS</div><span class="btn">Click Here</span></div>
  </div>
</section>

<div class="abs rule" style="top:952px"></div>

<section>
  <h2 class="abs section-title" style="top:996px">SKIN CARE PRODUCTS</h2>
  <div class="abs pager" style="left:988px;top:1004px">
    <i><svg width="10" height="10" viewBox="0 0 10 10"><path d="M6.5 1.5L3 5l3.5 3.5" stroke="#555" stroke-width="1.6" fill="none"/></svg></i>
    <i><svg width="10" height="10" viewBox="0 0 10 10"><path d="M3.5 1.5L7 5 3.5 8.5" stroke="#555" stroke-width="1.6" fill="none"/></svg></i>
  </div>
  <div class="abs product" style="left:152px;top:1080px">
    <div class="img" role="img" aria-label="Green skin care bottles with aloe leaves" style="background:linear-gradient(180deg,#f4f7f0,#dfe9d2)"></div>
    <div class="name">Product Name 1</div><div class="price">$ 61.19</div>
    <div class="stars">★★★★<b>★</b></div><span class="btn">Add to Cart</span>
  </div>
  <div class="abs product" style="left:384px;top:1080px">
    <div class="img" role="img" aria-label="White cream jars and bottles on a towel" style="background:linear-gradient(180deg,#f5f5f3,#e2e4dc)"></div>
    <div class="name">Product Name 2</div><div class="price">$ 61.19</div>
    <div class="stars">★★★★<b>★</b></div><span class="btn">Add to Cart</span>
  </div>
  <div class="abs babies" role="img" aria-label="Mother and baby resting on soft bedding"></div>
  <div class="abs babies-copy">
    <h3>FOR BABIES</h3><span class="btn">Shop Now</span>
  </div>
</section>

<div class="abs rule" style="top:1520px"></div>

<section>
  <h2 class="abs section-title" style="top:1552px">TOP PRODUCTS</h2>
  <div class="abs product" style="left:152px;top:1632px">
    <div class="img" role="img" aria-label="Amber serum bottle with green leaves" style="background:linear-gradient(180deg,#f4f4f2,#e4e6dd)"></div>
    <div class="name">Skin Product 1</div><div class="price">$ 61.19</div>
    <div class="stars">★★★★<b>★</b></div><span class="btn">Add to Cart</span>
  </div>
  <div class="abs product" style="left:384px;top:1632px">
    <div class="img" role="img" aria-label="White face cream tube" style="background:linear-gradient(180deg,#f6f6f6,#e6e6e6)"></div>
    <div class="name">Face Product 1</div><div class="price">$ 61.19</div>
    <div class="stars">★★★★<b>★</b></div><span class="btn">Add to Cart</span>
  </div>
  <div class="abs product" style="left:612px;top:1632px">
    <div class="img" role="img" aria-label="Green body lotion pump bottle" style="background:linear-gradient(180deg,#f3f6ef,#e1e9d6)"></div>
    <div class="name">Body Lotion 1</div><div class="price">$ 61.19</div>
    <div class="stars">★★★★<b>★</b></div><span class="btn">Add to Cart</span>
  </div>
  <div class="abs product" style="left:840px;top:1632px">
    <div class="img" role="img" aria-label="Baby care product box" style="background:linear-gradient(180deg,#f4f4f1,#e3e8da)"></div>
    <div class="name">Baby Product 1</div><div class="price">$ 61.19</div>
    <div class="stars">★★★★<b>★</b></div><span class="btn">Add to Cart</span>
  </div>
</section>

<div class="abs rule" style="top:2088px"></div>

<section>
  <div class="abs blog-band"></div>
  <h2 class="abs section-title" style="top:2144px">FROM THE BLOG</h2>
  <article class="abs post" style="left:152px;top:2220px">
    <div class="img" role="img" aria-label="Woman relaxing outdoors in sunlight" style="background:linear-gradient(135deg,#f1d9a8,#e8c49a)"><div class="date">02<small>DEC</small></div></div>
    <h4>CURABITUR LIGULASAPIEN</h4>
    <p>Vestibulum sagittis, nisl nec pellentesque suscipit, arcu leo rhoncus neque, vitae finibus velit odio eu lacus. Curabitur mattis nulla sed.</p>
  </article>
  <article class="abs post" style="left:460px;top:2220px">
    <div class="img" role="img" aria-label="Natural oils and herbs on a wooden table" style="background:linear-gradient(135deg,#f0e7dc,#c9b49a)"><div class="date">02<small>DEC</small></div></div>
    <h4>CURABITUR LIGULASAPIEN</h4>
    <p>Vestibulum sagittis, nisl nec pellentesque suscipit, arcu leo rhoncus neque, vitae finibus velit odio eu lacus. Curabitur mattis nulla sed.</p>
  </article>
  <article class="abs post" style="left:760px;top:2220px">
    <div class="img" role="img" aria-label="Parent massaging a baby with lotion" style="background:linear-gradient(135deg,#efd6c6,#d8b19a)"><div class="date">02<small>DEC</small></div></div>
    <h4>CURABITUR LIGULASAPIEN</h4>
    <p>Vestibulum sagittis, nisl nec pellentesque suscipit, arcu leo rhoncus neque, vitae finibus velit odio eu lacus. Curabitur mattis nulla sed.</p>
  </article>
</section>

<footer>
  <div class="abs footer"></div>
  <div class="abs f-logo wordmark"><i></i>Qelvora Store</div>
  <div class="abs newsletter">SIGN UP FOR OUR NEWSLETTER !</div>
  <div class="abs email">Email Address</div>
  <div class="abs submit">SUBMIT</div>
  <p class="abs f-about">Vestibulum sagittis, nisl nec pellentesque suscipit, arcu leo rhoncus neque, vitae finibus velit odio eu lacus. Curabitur mattis nulla sed porta.</p>
  <div class="abs f-col" style="left:420px;top:2700px">
    <h5>INFORMATION</h5>
    <ul><li>Careers</li><li>Product Catalogue</li><li>Press Releases</li><li>Shop with Points</li></ul>
  </div>
  <div class="abs f-col" style="left:620px;top:2700px">
    <h5>CUSTOMER CARE</h5>
    <ul><li>Returns</li><li>Shipping Info</li><li>Gift Cards</li><li>Size Guide</li></ul>
  </div>
  <div class="abs f-col info" style="left:792px;top:2680px;width:260px">
    <h5>STORE INFORMATION</h5>
    <ul>
      <li><svg width="12" height="14" viewBox="0 0 12 14"><path d="M6 13S1 8 1 5a5 5 0 0110 0c0 3-5 8-5 8z" fill="#5c9c22"/><circle cx="6" cy="5" r="1.8" fill="#fff"/></svg>18 Fernbrook Lane, Alderwick Green,<br>Hollowmere 40213</li>
      <li><svg width="13" height="10" viewBox="0 0 13 10"><rect x=".5" y=".5" width="12" height="9" fill="#5c9c22"/><path d="M1 1l5.5 4.5L12 1" stroke="#fff" fill="none"/></svg>hello@qelvorastore.co</li>
      <li><svg width="12" height="12" viewBox="0 0 12 12"><path d="M2 1l2.5 0 1 3-1.5 1a7 7 0 003 3l1-1.5 3 1V10a1 1 0 01-1 1A10 10 0 011 2a1 1 0 011-1z" fill="#5c9c22"/></svg>(555) 014-2280</li>
    </ul>
  </div>
  <div class="abs copyright">© 2020 Qelvora. All Rights Reserved</div>
</footer>

</body>
</html>
```